New Infographic Design Project

I need a 1 page Infographic that explains our Velqor Strand offer.

Can you use the following content in the attached document to create a 1 page infographic. The image in the bottom of the document is one of our competitors who is offering the same thing, this image is only provided for inspiration and ideas as we need ours to be based on the content of the document and aligned with the Bruvell Brand

```html
<!DOCTYPE html>
<html lang="en">
<head>
<meta charset="utf-8">
<title>Data Ready, AI Ready in 6 Weeks – Bruvell</title>
<link href="https://fonts.googleapis.com/css2?family=Outfit:wght@300;400;500;600;700;800&family=Audiowide&display=swap" rel="stylesheet">
<style>
:root{
  --backdrop:#b6b6b6;
  --red-deep:#6e0006;
  --red-mid:#a8000a;
  --red-bright:#f2111a;
  --accent:#ff2327;
  --icon:#e31b1f;
  --panel-dark:rgba(40,0,3,.82);
  --white:#ffffff;
  --ink:#1c1c1c;
  --ink-soft:#333333;
  --rule:#c9c9c9;
}
*{margin:0;padding:0;box-sizing:border-box}
html,body{width:1200px;height:908px;overflow:hidden}
body{background:var(--backdrop);font-family:"Outfit",sans-serif;position:relative}
.sheet{position:absolute;left:161px;top:144px;width:878px;height:621px;overflow:hidden;
  background:
    radial-gradient(ellipse 70% 60% at 100% 100%, var(--red-bright) 0%, rgba(242,17,26,0) 70%),
    linear-gradient(135deg,var(--red-deep) 0%,var(--red-mid) 45%,var(--red-bright) 100%);
  color:var(--white)}
.network-glow{position:absolute;left:0;top:360px;width:460px;height:261px;
  background:radial-gradient(ellipse at 30% 70%,rgba(255,70,70,.35) 0%,rgba(255,70,70,0) 65%)}
.abs{position:absolute}
.title{left:0;width:878px;top:26px;text-align:center;font-weight:700;font-size:51px;letter-spacing:.3px;line-height:1}
.title .hl{color:var(--accent)}
.tagline{left:0;width:878px;top:81px;text-align:center;font-weight:600;font-size:15.5px;letter-spacing:.2px}
.rule{height:1px;background:var(--white)}
.intro{left:36px;width:806px;top:103px;text-align:center;font-weight:300;font-size:12px;line-height:12px}

.edge{left:23px;top:149px;width:832px;height:136px;background:var(--white);border-radius:12px;color:var(--ink)}
.edge-title{left:0;width:832px;top:5px;text-align:center;font-weight:600;font-size:15.5px}
.edge-divider{top:35px;width:1px;height:90px;background:var(--rule)}
.edge-item{top:26px;width:200px;text-align:center}
.edge-item svg{display:block;margin:0 auto;width:44px;height:44px}
.edge-item h3{margin-top:10px;font-weight:500;font-size:9.6px;letter-spacing:.3px}
.edge-item p{margin-top:8px;font-weight:300;font-size:8.8px;line-height:12px;color:var(--ink-soft)}

.timeline{left:23px;top:296px;width:832px;height:180px;background:var(--panel-dark);border-radius:14px}
.timeline-title{left:0;width:832px;top:6px;text-align:center;font-weight:700;font-size:21.5px;letter-spacing:.3px}
.track{left:15px;top:91px;width:803px;height:3px;background:var(--white);border-radius:2px;box-shadow:0 0 0 1px var(--accent)}
.week{top:38px;width:124px;margin-left:-62px;text-align:center}
.week h4{font-family:"Audiowide",sans-serif;font-weight:400;font-size:16.5px;color:var(--accent);line-height:18px}
.week .phase{margin-top:1px;font-weight:400;font-size:10px;line-height:10px}
.week .dot{display:block;width:11px;height:11px;border-radius:50%;background:var(--accent);margin:8px auto 0}
.week p{margin-top:6px;font-weight:300;font-size:8.5px;line-height:11.2px}

.extra-title{left:0;width:878px;top:482px;text-align:center;font-weight:700;font-size:19px}
.card{top:522px;width:196px;height:79px;background:var(--white);color:var(--ink);border-radius:3px 3px 26px 3px;text-align:center;padding-top:13px}
.card h5{font-weight:600;font-size:9.6px}
.card p{margin:6px 10px 0;font-weight:300;font-size:8.5px;line-height:11.4px;color:var(--ink-soft)}
.badge{top:504px;width:24px;height:24px;margin-left:-12px}
</style>
</head>
<body>
<main class="sheet">
  <div class="network-glow" role="img" aria-label="Soft glowing network of connected nodes"></div>

  <h1 class="abs title">DATA READY, AI READY <span class="hl">IN 6 WEEKS</span></h1>
  <div class="abs rule" style="left:33px;top:87px;width:212px"></div>
  <div class="abs rule" style="left:632px;top:87px;width:213px"></div>
  <h2 class="abs tagline">YOUR LONG-TERM STRATEGIC DATA PARTNER</h2>
  <p class="abs intro">We start with a Business Data Assessment or Strand Deployment Assessment to pinpoint the highest-value use cases, the biggest data risks, and the fastest path to impact. We stand up a governed Velqor Strand foundation using repeatable ingestion, validation, and common data model patterns, so your reporting scales cleanly and your AI initiatives provide business value.</p>

  <section class="abs edge">
    <h2 class="abs edge-title">THE BRUVELL EDGE</h2>
    <div class="abs edge-divider" style="left:205px"></div>
    <div class="abs edge-divider" style="left:407px"></div>
    <div class="abs edge-divider" style="left:667px"></div>

    <div class="abs edge-item" style="left:-5px">
      <svg viewBox="0 0 44 44" fill="none" stroke="var(--icon)" stroke-width="1.6" stroke-linejoin="round">
        <path d="M12 10h26v22H12z M12 10l4-6h18l4 6 M21 4v12l4-3 4 3V4"/>
        <circle cx="12" cy="32" r="8" fill="#fff"/><circle cx="12" cy="32" r="5"/>
        <path d="M11 30l2-1v6"/>
      </svg>
      <h3>QUALITY-FIRST DELIVERY</h3>
      <p>Automated validation, data tests, and<br>“quality gates” that stop bad data upstream.</p>
    </div>
    <div class="abs edge-item" style="left:209px">
      <svg viewBox="0 0 44 44" fill="none" stroke="var(--icon)" stroke-width="1.6">
        <ellipse cx="19" cy="9" rx="15" ry="5"/>
        <path d="M4 9v24c0 3 7 5 15 5 M34 9v14 M4 17c0 3 7 5 15 5s15-2 15-5 M4 25c0 3 7 5 15 5"/>
        <circle cx="33" cy="33" r="7"/><path d="M28 38l10-10"/>
      </svg>
      <h3>DATA PRODUCTS, NOT DATASETS</h3>
      <p>Clear ownership, SLAs, versioning, and<br>reusable, consumable outputs aligned to<br>high impact business outcomes.</p>
    </div>
    <div class="abs edge-item" style="left:428px;width:246px">
      <svg viewBox="0 0 44 44" fill="none" stroke="var(--icon)" stroke-width="1.6" stroke-linejoin="round">
        <path d="M20 2v8 M20 2l6 2-6 2 M6 18a14 9 0 0 1 28 0z M4 18h32 M8 21v13 M14 21v13 M20 21v13 M26 21v9 M2 34h26 M2 38h26"/>
        <circle cx="34" cy="33" r="7"/><path d="M31 33l2 2 4-4"/>
      </svg>
      <h3>GOVERNANCE THAT DOESN'T SLOW YOU DOWN</h3>
      <p>Security, access, lineage, and auditability<br>built in from day one.</p>
    </div>
    <div class="abs edge-item" style="left:672px;width:160px">
      <svg viewBox="0 0 44 44" fill="none" stroke="var(--icon)" stroke-width="1.6">
        <path d="M22 3l3 4 5-1 1 5 5 2-2 5 3 4-4 3 1 5-5 1-2 5-5-2-4 3-3-4-5 1-1-5-5-2 2-5-3-4 4-3-1-5 5-1 2-5 5 2z"/>
        <path d="M16 22c0-4 3-6 6-6 4 0 5 6 8 6s4-2 4-4-2-3-3-3c-3 0-4 6-8 6-3 0-4-1-4-3"/>
      </svg>
      <h3>OPERATE SEAMLESSLY</h3>
      <p>CI/CD, monitoring, and cost controls<br>so the platform stays healthy.</p>
    </div>
  </section>

  <section class="abs timeline">
    <h2 class="abs timeline-title">6 WEEK TIME TO VALUE</h2>
    <div class="abs track"></div>
    <div class="abs week" style="left:75px"><h4>WEEK 1</h4><div class="phase">Envision<br>&amp; Assess</div><span class="dot"></span><p>Use case shortlist and priority based on highest business impact, current-state review, data risk &amp; compliance priorities, target operating model.</p></div>
    <div class="abs week" style="left:215px"><h4>WEEK 2</h4><div class="phase">Architecture<br>&amp; governance design</div><span class="dot"></span><p>Landing zone decisions, security and access model, patterns/standards, delivery plan and success metrics.</p></div>
    <div class="abs week" style="left:355px"><h4>WEEK 3</h4><div class="phase">Strand foundation<br>deployed</div><span class="dot"></span><p>Workspaces and environments, automation &amp; CI/CD, onboarding playbooks, baseline policies/guardrails.</p></div>
    <div class="abs week" style="left:479px"><h4>WEEK 4</h4><div class="phase">Data ingestion<br>+ validation framework</div><span class="dot"></span><p>Reusable ingestion patterns, automated validation, data contracts/SLAs, observability signals and alerting.</p></div>
    <div class="abs week" style="left:609px"><h4>WEEK 5</h4><div class="phase">Scalable common<br>data model</div><span class="dot"></span><p>Domain model, master entities, curated layer, semantic modelling patterns that support Clarion BI at scale.</p></div>
    <div class="abs week" style="left:750px;width:132px;margin-left:-66px"><h4>WEEK 6</h4><div class="phase">Business outcomes<br>+ AI-ready capability</div><span class="dot"></span><p>Executive dashboards and priority reports, performance optimisation, hypercare and handover, AI readiness check and pilot plan (predictive analytics and/or secure enterprise LLM).</p></div>
  </section>

  <div class="abs rule" style="left:33px;top:494px;width:324px"></div>
  <div class="abs rule" style="left:520px;top:494px;width:325px"></div>
  <h2 class="abs extra-title">EXTRA EDGE:</h2>

  <div class="abs card" style="left:22px"><h5>“AI-ready data” guarantee</h5><p>Every priority dataset ships with validation rules, ownership, lineage, and freshness SLAs before it can power AI.</p></div>
  <div class="abs card" style="left:234px"><h5>Cost-to-serve transparency</h5><p>Show business owners what each product/report costs to run and optimise it continuously.</p></div>
  <div class="abs card" style="left:447px"><h5>Change-proof pipelines</h5><p>Data contracts + automated tests reduce breakages from upstream schema changes.</p></div>
  <div class="abs card" style="left:659px"><h5>Governed self-serve</h5><p>Catalog + certified datasets so teams move faster without creating data chaos.</p></div>

  <svg class="abs badge" style="left:123px" viewBox="0 0 24 24"><circle cx="12" cy="12" r="11" fill="#fff" stroke="var(--icon)" stroke-width="1.4"/><circle cx="12" cy="12" r="6.5" fill="none" stroke="var(--icon)" stroke-width="1.4"/><path d="M9 12l2 2 4-4" fill="none" stroke="var(--icon)" stroke-width="1.5"/></svg>
  <svg class="abs badge" style="left:335px" viewBox="0 0 24 24"><circle cx="12" cy="12" r="11" fill="#fff" stroke="var(--icon)" stroke-width="1.4"/><circle cx="12" cy="12" r="6.5" fill="none" stroke="var(--icon)" stroke-width="1.4"/><path d="M9 12l2 2 4-4" fill="none" stroke="var(--icon)" stroke-width="1.5"/></svg>
  <svg class="abs badge" style="left:548px" viewBox="0 0 24 24"><circle cx="12" cy="12" r="11" fill="#fff" stroke="var(--icon)" stroke-width="1.4"/><circle cx="12" cy="12" r="6.5" fill="none" stroke="var(--icon)" stroke-width="1.4"/><path d="M9 12l2 2 4-4" fill="none" stroke="var(--icon)" stroke-width="1.5"/></svg>
  <svg class="abs badge" style="left:760px" viewBox="0 0 24 24"><circle cx="12" cy="12" r="11" fill="#fff" stroke="var(--icon)" stroke-width="1.4"/><circle cx="12" cy="12" r="6.5" fill="none" stroke="var(--icon)" stroke-width="1.4"/><path d="M9 12l2 2 4-4" fill="none" stroke="var(--icon)" stroke-width="1.5"/></svg>
</main>
</body>
</html>
```